7 Elite Label

Design a label for 7 Elite styling gels. The logo is attached. The color is C=100, M=100, Y=0, K=0. The 16 oz. jar is also attached.

Updates

Attention all designers,

The old logo has been deleted.  I have uploaded a new logo for this project.  Can you please update your design with the NEW LOGO?
thank you,
Rob

Target Market(s)

Multicultural

Requirements
Must have
• you must used the logo attached.

text to be included on the jar:

Used by Professionals
Maximum Hold
Alcohol Free
NO FLAKING

16 oz.

As far as label size, use the jar photo, and fit the design on it.

```html
<!DOCTYPE html>
<html lang="en">
<head>
<meta charset="utf-8">
<title>7 Elite Styling Gel Label</title>
<link rel="stylesheet" href="https://fonts.googleapis.com/css2?family=Cormorant+Garamond:ital,wght@1,600&display=swap">
<style>
  :root {
    --brand-blue: #2e3192;
    --circle-white: #fbfbfb;
    --bg-warm: #f1efe6;
    --bg-mid: #d9dbe0;
    --bg-cool: #c3c6d0;
  }
  html, body {
    margin: 0;
    padding: 0;
    width: 1200px;
    height: 661px;
    overflow: hidden;
  }
  .label {
    position: relative;
    width: 1200px;
    height: 661px;
    overflow: hidden;
    font-family: "Cormorant Garamond", Georgia, serif;
    font-style: italic;
    font-weight: 600;
    color: var(--brand-blue);
  }
  .label__backdrop {
    position: absolute;
    inset: 0;
    background:
      radial-gradient(ellipse 55% 70% at 42% 40%, rgba(255,255,240,0.85), rgba(255,255,240,0) 70%),
      linear-gradient(100deg, var(--bg-warm) 0%, var(--bg-mid) 55%, var(--bg-cool) 100%);
  }
  .label__seal {
    position: absolute;
    left: -228px;
    top: -72px;
    width: 806px;
    height: 806px;
    border-radius: 50%;
    background: var(--circle-white);
    box-shadow: 0 0 18px rgba(120,120,130,0.25);
  }
  .label__brand {
    position: absolute;
    left: 0;
    top: 220px;
    width: 360px;
    text-align: center;
    font-size: 118px;
    line-height: 1;
    margin: 0;
  }
  .label__claims {
    position: absolute;
    left: 640px;
    top: 78px;
    width: 500px;
    margin: 0;
    padding: 0;
    list-style: none;
    text-align: center;
    font-size: 60px;
    line-height: 68px;
  }
  .label__size {
    position: absolute;
    left: 640px;
    top: 538px;
    width: 500px;
    margin: 0;
    text-align: center;
    font-size: 60px;
    line-height: 68px;
  }
</style>
</head>
<body>
  <main class="label">
    <div class="label__backdrop" role="img" aria-label="Soft grey-blue damask flourish pattern"></div>
    <div class="label__seal"></div>
    <h1 class="label__brand">7 Elite</h1>
    <ul class="label__claims">
      <li>Used by Professionals</li>
      <li>Maximum Hold</li>
      <li>Alcohol Free</li>
      <li>No Flaking</li>
    </ul>
    <p class="label__size">8 oz.</p>
  </main>
</body>
</html>
```